SAVOR food + music festival poster

11x17 poster design for our food & music festival in Lexington, KY. The two-day festival is a celebration of all things local and over 20,000 people attend each year. Over 50 local food vendors and food trucks, local music, craft beer and cocktails, a car show, kids activities, art etc. www.savorfestplex.com. Attached is our logo, and variation thereof. We prefer the black text with yellow "nom" as well call him. Images: https://shortlinkr.com/q4kd9wza and https://shortlinkr.com/p7ht2mue and https://shortlinkr.com/r3vn8bqc and https://shortlinkr.com/w5jx1fsd

Target Market(s)

People who would want to attend a food and music festival

Industry/Entity Type

Festival

Font styles to use
Sans Serif

Colors

Designer to choose colors to be used in the design.

Requirements
Must have
• (savor logo)
• food + music festival
• AUGUST 11 & 12, 2018
• Cedarline Showgrounds at Harwick Meadow Park
• 50+ Local Restaurants & Food Trucks • Live Music
• Classic Car Show • Craft Beer & Cocktails
• Kids Activities & More!
• (small) Produced by (Brindle Oak Publishing Logo)
• Design style: Think, modern, hip, fun, local
Nice to have
• small area for sponsor logos
Should not have
• Design style: NOT county fair

```html
<!DOCTYPE html>
<html lang="en">
<head>
<meta charset="utf-8">
<title>SAVOR Food + Music Festival</title>
<link rel="stylesheet" href="https://fonts.googleapis.com/css2?family=Montserrat:wght@600;700&family=Dancing+Script:wght@500&display=swap">
<style>
  :root{
    --ink:#2b2b2b;
    --gold:#f5ae2e;
    --pink:#e8559a;
    --frame:#dcdcdc;
    --sponsor-red:#e32222;
    --mint:#8fd3c8;
    --rose:#f08aa0;
    --lilac:#c59be0;
    --peach:#f6b26b;
    --sky:#9ec9ef;
    --tan:#c9aa95;
    --paper:#ffffff;
  }
  *{margin:0;padding:0;box-sizing:border-box}
  html,body{width:777px;height:1200px;overflow:hidden;background:var(--paper)}
  .poster{position:relative;width:777px;height:1200px;overflow:hidden;background:var(--paper);font-family:"Montserrat",Arial,sans-serif;color:var(--ink)}
  .artwork{position:absolute;inset:0}
  .brand{position:absolute;left:0;width:600px;text-align:center}
  .brand-mark{position:absolute;left:254px;top:120px;width:92px;height:92px;border-radius:50%;border:9px solid var(--gold)}
  .brand-name{top:222px;left:0;width:600px;font-weight:700;font-size:118px;letter-spacing:16px;line-height:1;color:var(--ink);padding-left:16px}
  .tagline{top:332px;font-weight:700;font-size:34.5px;color:var(--gold);letter-spacing:.6px;line-height:1}
  .venue{top:378px;font-weight:700;font-size:16.5px;line-height:22px;letter-spacing:.3px}
  .date{position:absolute;left:120px;top:426px;width:349px;height:36px;background:var(--gold);color:#fff;font-weight:700;font-size:28px;line-height:37px;text-align:center;letter-spacing:.5px}
  .highlights{position:absolute;left:30px;top:489px;list-style:none}
  .highlights li{display:flex;align-items:center;font-weight:600;font-size:26px;line-height:1;height:30px;margin-bottom:12.5px;white-space:nowrap}
  .highlights li::before,.highlights li::after{content:"";width:6px;height:24px;border-left:2px solid var(--c);border-right:2px solid var(--c);transform:skewX(-8deg);opacity:.8}
  .highlights li::before{margin-right:4px}
  .highlights li::after{margin-left:4px}
  .hl-food{--c:var(--mint)}
  .hl-drinks{--c:var(--rose)}
  .hl-cars{--c:var(--sky)}
  .hl-music{--c:var(--tan)}
  .hl-kids{--c:var(--peach)}
  .footer{position:absolute;left:0;top:1132px;width:777px;height:68px;background:var(--paper)}
  .producer{position:absolute;left:14px;top:3px;width:66px;text-align:center}
  .producer-label{font-family:"Dancing Script",cursive;font-size:12px;line-height:14px;color:var(--ink)}
  .producer-badge{display:block;width:28px;height:28px;margin:2px auto 1px;border-radius:50%;border:3px solid var(--ink)}
  .producer-name{font-size:6.5px;font-weight:700;line-height:8px}
  .sponsors{position:absolute;left:270px;top:18px;width:310px;text-align:center;font-family:Arial,Helvetica,sans-serif;font-size:23px;color:var(--sponsor-red)}
</style>
</head>
<body>
<main class="poster">
  <svg class="artwork" width="777" height="1200" viewBox="0 0 777 1200" xmlns="http://www.w3.org/2000/svg">
    <defs>
      <radialGradient id="splash" cx="50%" cy="50%" r="50%">
        <stop offset="0" stop-color="#a72c8f"/>
        <stop offset=".6" stop-color="#d65aa8" stop-opacity=".85"/>
        <stop offset="1" stop-color="#f0a0cc" stop-opacity="0"/>
      </radialGradient>
      <linearGradient id="crowd" x1="0" y1="0" x2="0" y2="1">
        <stop offset="0" stop-color="#e6eef3"/><stop offset=".28" stop-color="#e6eef3"/>
        <stop offset=".3" stop-color="#8aa366"/><stop offset=".45" stop-color="#b58a8a"/>
        <stop offset=".6" stop-color="#7f9a52"/><stop offset="1" stop-color="#6a8a3c"/>
      </linearGradient>
      <linearGradient id="child" x1="0" y1="0" x2="1" y2="1">
        <stop offset="0" stop-color="#b9a28f"/><stop offset=".5" stop-color="#e4cdbd"/><stop offset="1" stop-color="#8e8f9a"/>
      </linearGradient>
      <linearGradient id="car" x1="0" y1="0" x2="0" y2="1">
        <stop offset="0" stop-color="#b8d3ea"/><stop offset=".3" stop-color="#b8d3ea"/>
        <stop offset=".32" stop-color="#5f7e45"/><stop offset=".45" stop-color="#5f7e45"/>
        <stop offset=".47" stop-color="#23293a"/><stop offset=".75" stop-color="#23293a"/>
        <stop offset=".77" stop-color="#78984a"/><stop offset="1" stop-color="#78984a"/>
      </linearGradient>
      <linearGradient id="grill" x1="0" y1="0" x2="0" y2="1">
        <stop offset="0" stop-color="#8ea86a"/><stop offset=".22" stop-color="#8ea86a"/>
        <stop offset=".24" stop-color="#b0603a"/><stop offset=".7" stop-color="#7a3a22"/><stop offset="1" stop-color="#241a16"/>
      </linearGradient>
      <linearGradient id="hooper" x1="0" y1="0" x2="0" y2="1">
        <stop offset="0" stop-color="#e9cbb8"/><stop offset=".45" stop-color="#e7b7a6"/><stop offset=".55" stop-color="#e0463a"/><stop offset="1" stop-color="#d83a30"/>
      </linearGradient>
    </defs>

    <g class="eq-top" stroke-linecap="round" stroke-width="7">
      <line x1="4" y1="0" x2="4" y2="62" stroke="#8fd3c8"/>
      <line x1="17" y1="0" x2="17" y2="40" stroke="#9ec9ef"/>
      <line x1="30" y1="0" x2="30" y2="78" stroke="#c59be0"/>
      <line x1="43" y1="0" x2="43" y2="50" stroke="#f08aa0"/>
      <line x1="56" y1="0" x2="56" y2="70" stroke="#f6b26b"/>
      <line x1="69" y1="0" x2="69" y2="34" stroke="#8fd3c8"/>
      <line x1="82" y1="0" x2="82" y2="66" stroke="#e97fb3"/>
      <line x1="95" y1="0" x2="95" y2="46" stroke="#b9a0e6"/>
      <line x1="108" y1="0" x2="108" y2="74" stroke="#9ec9ef"/>
      <line x1="121" y1="0" x2="121" y2="56" stroke="#f4a6a0"/>
      <line x1="134" y1="0" x2="134" y2="30" stroke="#c59be0"/>
      <line x1="147" y1="0" x2="147" y2="68" stroke="#f08aa0"/>
      <line x1="160" y1="0" x2="160" y2="44" stroke="#8fd3c8"/>
      <line x1="173" y1="0" x2="173" y2="76" stroke="#f6b26b"/>
      <line x1="186" y1="0" x2="186" y2="52" stroke="#e97fb3"/>
      <line x1="199" y1="0" x2="199" y2="64" stroke="#9ec9ef"/>
      <line x1="212" y1="0" x2="212" y2="36" stroke="#b9a0e6"/>
      <line x1="225" y1="0" x2="225" y2="72" stroke="#f08aa0"/>
      <line x1="238" y1="0" x2="238" y2="48" stroke="#8fd3c8"/>
      <line x1="251" y1="0" x2="251" y2="60" stroke="#c59be0"/>
      <line x1="264" y1="0" x2="264" y2="80" stroke="#f4a6a0"/>
      <line x1="277" y1="0" x2="277" y2="42" stroke="#9ec9ef"/>
      <line x1="290" y1="0" x2="290" y2="66" stroke="#e97fb3"/>
      <line x1="303" y1="0" x2="303" y2="54" stroke="#f6b26b"/>
      <line x1="316" y1="0" x2="316" y2="74" stroke="#b9a0e6"/>
      <line x1="329" y1="0" x2="329" y2="38" stroke="#8fd3c8"/>
      <line x1="342" y1="0" x2="342" y2="62" stroke="#f08aa0"/>
      <line x1="355" y1="0" x2="355" y2="48" stroke="#9ec9ef"/>
      <line x1="368" y1="0" x2="368" y2="70" stroke="#c59be0"/>
      <line x1="381" y1="0" x2="381" y2="32" stroke="#f4a6a0"/>
      <line x1="394" y1="0" x2="394" y2="64" stroke="#e97fb3"/>
      <line x1="407" y1="0" x2="407" y2="50" stroke="#8fd3c8"/>
      <line x1="420" y1="0" x2="420" y2="76" stroke="#b9a0e6"/>
      <line x1="433" y1="0" x2="433" y2="44" stroke="#f6b26b"/>
      <line x1="446" y1="0" x2="446" y2="68" stroke="#9ec9ef"/>
      <line x1="459" y1="0" x2="459" y2="36" stroke="#f08aa0"/>
      <line x1="472" y1="0" x2="472" y2="58" stroke="#c59be0"/>
      <line x1="485" y1="0" x2="485" y2="72" stroke="#8fd3c8"/>
      <line x1="498" y1="0" x2="498" y2="40" stroke="#e97fb3"/>
      <line x1="511" y1="0" x2="511" y2="62" stroke="#f4a6a0"/>
      <line x1="524" y1="0" x2="524" y2="46" stroke="#9ec9ef"/>
      <line x1="537" y1="0" x2="537" y2="66" stroke="#b9a0e6"/>
      <line x1="550" y1="0" x2="550" y2="30" stroke="#f6b26b"/>
      <line x1="563" y1="0" x2="563" y2="54" stroke="#c59be0"/>
      <line x1="576" y1="0" x2="576" y2="38" stroke="#f08aa0"/>
      <line x1="589" y1="0" x2="589" y2="24" stroke="#8fd3c8"/>
    </g>

    <g role="img" aria-label="Purple and pink paint splash with white icons of a cocktail, treble clef, hat and clock">
      <ellipse cx="676" cy="120" rx="112" ry="150" fill="url(#splash)"/>
    </g>

    <g class="eq-bottom">
      <rect x="4" y="1052" width="8" height="80" fill="#9ec9ef"/>
      <rect x="18" y="1078" width="8" height="54" fill="#8fd3c8"/>
      <rect x="150" y="1070" width="8" height="62" fill="#f08aa0"/>
      <rect x="164" y="1090" width="8" height="42" fill="#f6b26b"/>
      <rect x="178" y="1058" width="8" height="74" fill="#e97fb3"/>
      <rect x="192" y="1080" width="8" height="52" fill="#f4a6a0"/>
      <rect x="206" y="1064" width="8" height="68" fill="#d94f7a"/>
      <rect x="220" y="1040" width="8" height="92" fill="#e97fb3"/>
      <rect x="234" y="1074" width="8" height="58" fill="#f08aa0"/>
      <rect x="248" y="1048" width="8" height="84" fill="#f6b26b"/>
      <rect x="262" y="1068" width="8" height="64" fill="#c9aa95"/>
      <rect x="276" y="1052" width="8" height="80" fill="#e97fb3"/>
      <rect x="290" y="1082" width="8" height="50" fill="#f4a6a0"/>
      <rect x="304" y="1060" width="8" height="72" fill="#d98ab0"/>
      <rect x="318" y="1044" width="8" height="88" fill="#f08aa0"/>
      <rect x="332" y="1072" width="8" height="60" fill="#f6b26b"/>
      <rect x="346" y="1056" width="8" height="76" fill="#e97fb3"/>
      <rect x="360" y="1086" width="8" height="46" fill="#c59be0"/>
      <rect x="374" y="1062" width="8" height="70" fill="#d98ab0"/>
      <rect x="388" y="1034" width="8" height="98" fill="#e97fb3"/>
      <rect x="402" y="1070" width="8" height="62" fill="#f4a6a0"/>
      <rect x="416" y="1050" width="8" height="82" fill="#b9a0e6"/>
      <rect x="430" y="1078" width="8" height="54" fill="#c59be0"/>
      <rect x="444" y="1062" width="8" height="70" fill="#9ec9ef"/>
      <rect x="458" y="1086" width="8" height="46" fill="#b9a0e6"/>
      <rect x="472" y="1056" width="8" height="76" fill="#c59be0"/>
      <rect x="556" y="1074" width="8" height="58" fill="#9ec9ef"/>
      <rect x="570" y="1090" width="8" height="42" fill="#b9a0e6"/>
      <rect x="584" y="1066" width="8" height="66" fill="#c59be0"/>
      <rect x="598" y="1082" width="8" height="50" fill="#9ec9ef"/>
      <rect x="612" y="1070" width="8" height="62" fill="#b9a0e6"/>
    </g>

    <g role="img" aria-label="Purple and pink paint splash">
      <ellipse cx="500" cy="630" rx="82" ry="66" fill="url(#splash)"/>
    </g>

    <g class="photo-cluster">
      <circle cx="700" cy="766" r="186" fill="var(--pink)"/>
      <circle cx="420" cy="780" r="94" fill="var(--pink)"/>
      <circle cx="508" cy="956" r="92" fill="var(--pink)"/>
      <circle cx="692" cy="1016" r="94" fill="var(--pink)"/>
      <polygon points="500,846 540,880 486,884" fill="var(--pink)"/>
      <polygon points="596,920 626,948 598,956" fill="var(--pink)"/>

      <circle cx="690" cy="762" r="156" fill="var(--frame)"/>
      <circle cx="690" cy="762" r="148" fill="url(#crowd)" role="img" aria-label="Photo of a festival crowd on a lawn with drummers playing"/>
      <circle cx="420" cy="780" r="86" fill="var(--frame)"/>
      <circle cx="420" cy="780" r="80" fill="url(#child)" role="img" aria-label="Photo of a child with face paint and a flower crown"/>
      <circle cx="508" cy="956" r="84" fill="var(--frame)"/>
      <circle cx="508" cy="956" r="78" fill="url(#car)" role="img" aria-label="Photo of a classic car at the car show"/>
      <circle cx="692" cy="1016" r="86" fill="var(--frame)"/>
      <circle cx="692" cy="1016" r="80" fill="url(#grill)" role="img" aria-label="Photo of food cooking on a large grill"/>
    </g>

    <g class="dots">
      <circle cx="324" cy="720" r="6" fill="#e4155b"/>
      <circle cx="375" cy="914" r="25" fill="#f8b9a0"/>
      <circle cx="388" cy="962" r="11" fill="#fbd08a"/>
      <circle cx="580" cy="1050" r="10" fill="#f6b26b"/>
      <circle cx="580" cy="1026" r="7" fill="#e4155b"/>
      <circle cx="765" cy="1118" r="14" fill="#fbd08a"/>
    </g>

    <g class="hooper-cutout" role="img" aria-label="Cut-out photo of a woman in sunglasses and red trousers dancing with a hula hoop">
      <rect x="40" y="834" width="250" height="298" rx="30" fill="url(#hooper)" stroke="#e6a9d6" stroke-width="4"/>
    </g>
  </svg>

  <div class="brand-mark" aria-hidden="true"></div>
  <h1 class="brand brand-name">SAVOR</h1>
  <p class="brand tagline">FOOD + MUSIC FESTIVAL</p>
  <p class="brand venue">CEDARLINE SHOWGROUNDS @ HARWICK MEADOW PARK<br>LEXINGTON, KY</p>
  <p class="date">AUGUST 11-12, 2018</p>

  <ul class="highlights">
    <li class="hl-food">50+ Local Restaurants &amp; Food Trucks</li>
    <li class="hl-drinks">Craft Beer &amp; Cocktails</li>
    <li class="hl-cars">Classic Car Show</li>
    <li class="hl-music">Live Music</li>
    <li class="hl-kids">Kids Activities &amp; More!</li>
  </ul>

  <footer class="footer">
    <div class="producer">
      <div class="producer-label">Powered by</div>
      <span class="producer-badge" aria-hidden="true"></span>
      <div class="producer-name">Brindle Oak Publishing</div>
    </div>
    <p class="sponsors">SPONSORS LOGO AREA</p>
  </footer>
</main>
</body>
</html>
```